Wordpress coded website (5 page-home page, contact form & 3 common pages) for Skiing event

I would like a WordPress site designed for our Ski & Snowboard event. The site is to have 5 total pages.

Hosting has been setup (Brightleaf Hosting) and WordPress installed.

Requirements:
Front page with Landscape slide, Snowpost feed, 4 menu items, footer and small description section.

3 Separate pages to be created, with a similar layout with landscape image slider and large text section (content provided)

1 Contact us page with the below form sections
- Name
- School
- Position
- Email
- Phone
- Message

Target Market(s)

School teachers and school students

Industry/Entity Type

Tourism

Number of Pages Required

5+ page

Colors

Designer to choose colors to be used in the design.

Requirements
Must have
• Must include event logo attached in brief. Must include Snowpost feed on homepage

```html
<!DOCTYPE html>
<html lang="en">
<head>
<meta charset="utf-8">
<title>Mount Harlow Ski Challenge</title>
<link href="https://fonts.googleapis.com/css2?family=Lato:wght@400;700;900&display=swap" rel="stylesheet">
<style>
:root{
  --blue:#0d96e3;
  --ink:#222;
  --text:#333;
  --dark:#1d1d1d;
  --darker:#121212;
  --feed:#3a5795;
  --rule:#cfcfcf;
  --white:#fff;
}
*{box-sizing:border-box;margin:0;padding:0}
html,body{width:1017px;height:1200px;overflow:hidden;background:var(--white)}
body{position:relative;font-family:'Lato',sans-serif;color:var(--text)}
.abs{position:absolute}

/* header */
.site-header{position:absolute;left:0;top:0;width:1017px;height:113px;background:var(--white);border-top:2px solid #333}
.contact-strip{position:absolute;top:0;left:515px;height:30px;display:flex}
.contact-strip .mail{background:#2a2a2a;color:var(--white);padding:0 16px 0 20px;display:flex;align-items:center;gap:8px;font-size:13.5px;clip-path:polygon(0 0,100% 0,100% 100%,6% 100%)}
.contact-strip .phone{background:var(--blue);color:var(--white);padding:0 24px 0 14px;display:flex;align-items:center;gap:8px;font-size:13.5px;clip-path:polygon(0 0,100% 0,92% 100%,0 100%)}
.strip-icon{width:18px;height:18px;border-radius:50%;background:var(--white);display:flex;align-items:center;justify-content:center}
.brand{position:absolute;left:83px;top:0;width:150px;height:175px;background:var(--white);box-shadow:0 2px 6px rgba(0,0,0,.12);z-index:3;display:flex;flex-direction:column;align-items:center;justify-content:center;gap:10px;clip-path:polygon(0 0,100% 0,100% 86%,50% 100%,0 86%)}
.brand-dot{width:34px;height:34px;border-radius:50%;background:var(--blue)}
.brand-name{font-weight:700;font-size:17px;line-height:1.15;color:var(--blue);text-align:center}
.main-nav{position:absolute;top:62px;left:400px;display:flex;align-items:center}
.main-nav a{font-size:15px;color:var(--ink);text-decoration:none;padding:0 33px;border-left:1px solid #ddd;line-height:16px}
.main-nav a:first-child{border-left:0;color:var(--blue);font-weight:700;position:relative}
.main-nav a:first-child::after{content:"";position:absolute;left:50%;top:24px;width:12px;height:12px;margin-left:-6px;border-radius:50%;background:var(--blue)}

/* hero */
.hero{position:absolute;left:0;top:113px;width:1017px;height:462px;background:linear-gradient(90deg,#3e3e40 0%,#6c6c70 35%,#c7a9b8 62%,#b55a8e 78%,#6e6e72 100%)}
.hero-title{position:absolute;left:100px;top:165px;width:420px;text-align:center;color:var(--white);font-weight:700;font-size:44px;line-height:52px;text-shadow:0 2px 6px rgba(0,0,0,.45)}
.hero-arrow{position:absolute;top:217px;width:36px;height:36px;background:#3a3a3a;display:flex;align-items:center;justify-content:center}
.hero-arrow.prev{left:26px}
.hero-arrow.next{left:955px;background:#6a6a6a}

/* about */
.about{position:absolute;left:84px;top:612px;width:590px}
.about h1{font-size:28px;font-weight:700;color:var(--blue);letter-spacing:-.2px}
.about-divider{position:relative;height:26px;margin-top:12px}
.about-divider span{position:absolute;left:0;top:2px;width:18px;height:20px;border-radius:50%;background:#c9c9c9}
.about-divider i{position:absolute;left:32px;right:-2px;top:12px;border-top:1px solid var(--rule);border-bottom:1px solid #eee}
.about .date{font-weight:700;color:var(--ink);font-size:13.5px;margin-top:16px}
.about p{font-size:13.5px;line-height:23.6px;color:var(--text)}
.about .note{margin-top:5px}
.about .note b{color:var(--ink)}

/* feed */
.feed{position:absolute;left:711px;top:619px;width:222px;height:249px;border:2px solid var(--feed);background:var(--white)}
.feed-head{height:31px;background:var(--feed);color:var(--white);display:flex;justify-content:space-between;align-items:center;padding:0 12px;font-size:11.5px}
.feed-head b{font-weight:900;font-size:11.5px}
.feed-item{display:flex;gap:9px;margin:0 10px;padding:10px 0 8px;border-bottom:1px dotted #ccc}
.feed-thumb{width:43px;height:36px;flex:none;background:linear-gradient(135deg,#456c8a,#c9b48c)}
.feed-item a{display:block;color:#3b64a8;font-size:10.2px;line-height:14.5px;text-decoration:none}
.feed-item small{display:block;font-size:8px;color:#333;margin-top:3px}
.feed-foot{position:absolute;bottom:0;left:0;right:0;border-top:1px solid #ddd;padding:7px 10px;font-size:9.5px;color:#555}

/* footer */
.site-footer{position:absolute;left:0;top:912px;width:1017px;height:251px;background:var(--dark);color:var(--white)}
.footer-col{position:absolute;top:30px}
.footer-col h3{font-size:17px;font-weight:400;letter-spacing:.2px}
.footer-col h3 em{font-style:normal;color:var(--blue)}
.footer-col .rule{margin-top:9px;border-top:1px solid #4a4a4a;position:relative}
.footer-col .rule::before{content:"";position:absolute;left:0;top:-2px;width:24px;border-top:2px solid #777}
.col-sep{position:absolute;top:45px;height:175px;border-left:1px solid #333}
.quick-links ul{list-style:none;margin-top:6px}
.quick-links li{font-size:13.5px;line-height:30px;padding-left:2px}
.quick-links li::before{content:"•";font-size:10px;margin-right:6px}
.contact-details .org{font-weight:700;font-size:14px;margin-top:10px}
.contact-details .addr{font-size:11px;line-height:17.5px}
.contact-row{display:flex;align-items:center;gap:11px;font-size:11.5px;margin-top:14px}
.contact-row svg{width:13px;height:13px;flex:none}
.inquiry-field{width:218px;height:29px;border:1px solid #444;background:#181818;color:#ddd;font-size:11px;padding:0 10px;display:flex;align-items:center;margin-top:6px}
.inquiry-field:first-of-type{margin-top:12px}
.inquiry-field.message{height:36px;align-items:flex-start;padding-top:7px}
.submit{margin-top:7px;width:87px;height:29px;background:var(--blue);color:var(--white);font-size:13.5px;font-weight:700;display:flex;align-items:center;justify-content:center;letter-spacing:.5px}
.footer-brand{position:absolute;left:795px;top:50px;width:136px;height:170px;display:flex;flex-direction:column;align-items:center;justify-content:center;gap:12px}
.footer-brand .dot{width:40px;height:40px;border-radius:50%;background:#8a8a8a}
.footer-brand .name{font-weight:700;font-size:19px;line-height:1.2;color:#a8a8a8;text-align:center}
.bottom-bar{position:absolute;left:0;top:1163px;width:1017px;height:37px;background:var(--darker);color:var(--white);font-size:11.5px}
.bottom-bar p{position:absolute;left:85px;top:11px}
.social{position:absolute;top:8px;display:flex;gap:7px;left:832px}
.social span{width:20px;height:20px;border-radius:50%;background:var(--white)}
</style>
</head>
<body>

<header class="site-header">
  <div class="contact-strip">
    <div class="mail"><span class="strip-icon"><svg width="10" height="8" viewBox="0 0 10 8"><rect x=".5" y=".5" width="9" height="7" fill="none" stroke="#2a2a2a"/><path d="M.5 .5 5 4.5 9.5 .5" fill="none" stroke="#2a2a2a"/></svg></span>hello@harlowskichallenge.example</div>
    <div class="phone"><span class="strip-icon"><svg width="10" height="8" viewBox="0 0 10 8"><rect x=".5" y=".5" width="9" height="7" fill="none" stroke="#0d96e3"/><path d="M.5 .5 5 4.5 9.5 .5" fill="none" stroke="#0d96e3"/></svg></span>02 5550 1842</div>
  </div>
  <div class="brand"><span class="brand-dot"></span><span class="brand-name">Mount Harlow<br>Ski Challenge</span></div>
  <nav class="main-nav">
    <a href="#">Home</a><a href="#">Event</a><a href="#">Mt Harlow</a><a href="#">Itinerary</a><a href="#">Contact Us</a>
  </nav>
</header>

<section class="hero" role="img" aria-label="Photo of a young skier in a pink helmet and goggles on a snowy slope">
  <h2 class="hero-title">Welcome To<br>About Mount Harlow<br>Ski Challenge</h2>
  <span class="hero-arrow prev"><svg width="10" height="14" viewBox="0 0 10 14"><path d="M8 1 2 7l6 6" fill="none" stroke="#fff" stroke-width="2"/></svg></span>
  <span class="hero-arrow next"><svg width="10" height="14" viewBox="0 0 10 14"><path d="M2 1l6 6-6 6" fill="none" stroke="#fff" stroke-width="2"/></svg></span>
</section>

<section class="about">
  <h1>About Mount Harlow Ski Challenge</h1>
  <div class="about-divider"><span></span><i></i></div>
  <p class="date">Wednesday 11th July &amp; Thursday 12th July 2018.</p>
  <p>The Mt Harlow Ski Challenge is the first event of its kind in the Southern Hemisphere offering high school students from Australia to face off against New Zealand locals on the ski fields of Mt Harlow. With no race experience necessary, the event provides a great fun experience for those enjoying their first time on the slopes as well as providing a chance for experienced skiers and snowboarders to test themselves against the clock and other competitors.</p>
  <p class="note"><b>Notes:</b> No experience necessary badge to appear on page</p>
</section>

<aside class="feed">
  <div class="feed-head"><span>Recent Activity</span><b>Snowpost</b></div>
  <div class="feed-item"><span class="feed-thumb" role="img" aria-label="Thumbnail of a lodge building"></span><div><a href="#">Lorem ipsum dolor sit amet the consectetuer adipi.</a><small>2 people recommended this.</small></div></div>
  <div class="feed-item"><span class="feed-thumb" role="img" aria-label="Thumbnail of ski gear"></span><div><a href="#">Lorem ipsum dolor sit amet the adipiscing elit, sed di nonummy</a><small>3 people recommended this.</small></div></div>
  <div class="feed-item" style="border-bottom:0"><span class="feed-thumb" role="img" aria-label="Thumbnail of a skier"></span><div><a href="#">Lorem ipsum dolor sit amet the consectetuer adipiscing.</a><small>2 people recommended this.</small></div></div>
  <div class="feed-foot">Snowpost Social Plugin</div>
</aside>

<footer class="site-footer">
  <div class="footer-col quick-links" style="left:83px;width:111px">
    <h3>QUICK <em>LINKS</em></h3><div class="rule"></div>
    <ul><li>Home</li><li>Event</li><li>Mt Harlow</li><li>Itinerary</li><li>Contact Us</li></ul>
  </div>
  <span class="col-sep" style="left:221px"></span>
  <div class="footer-col contact-details" style="left:252px;width:206px">
    <h3>CONTACT <em>DETAILS</em></h3><div class="rule"></div>
    <p class="org">Mount Harlow Ski Challenge</p>
    <p class="addr">88 Alpine Road, Glenvale,<br>Glenvale - 40512</p>
    <div class="contact-row" style="margin-top:16px"><svg viewBox="0 0 13 13"><path d="M3 1 5 4 3.8 5.5Q5 8 7.5 9.2L9 8l3 2-1 2Q7 12.5 3.5 9 .5 5.5 1 2Z" fill="#fff"/></svg>02 5550 1842</div>
    <div class="contact-row"><svg viewBox="0 0 13 13"><rect x="3" y="1" width="7" height="4" fill="#fff"/><rect x="1" y="5" width="11" height="5" rx="1" fill="#fff"/><rect x="3" y="9" width="7" height="3" fill="#fff" stroke="#1d1d1d"/></svg>02 5550 1843</div>
    <div class="contact-row"><svg viewBox="0 0 13 13"><rect x="1" y="3" width="11" height="7" fill="#fff"/><path d="M1 3l5.5 4L12 3" fill="none" stroke="#1d1d1d"/></svg>hello@harlowskichallenge.example</div>
  </div>
  <span class="col-sep" style="left:485px"></span>
  <div class="footer-col quick-inquiry" style="left:516px;width:220px">
    <h3>QUICK <em>INQUIRY</em></h3><div class="rule"></div>
    <div class="inquiry-field">Name</div>
    <div class="inquiry-field">Email</div>
    <div class="inquiry-field message">Message</div>
    <div class="submit">SUBMIT</div>
  </div>
  <span class="col-sep" style="left:765px"></span>
  <div class="footer-brand"><span class="dot"></span><span class="name">Mount Harlow<br>Ski Challenge</span></div>
</footer>

<div class="bottom-bar">
  <p>Copyright © 2017 Mount Harlow Ski Challenge. All Right Reserved.</p>
  <div class="social"><span></span><span></span><span></span><span></span></div>
</div>

</body>
</html>
```